Popup Banners - BrightCounsel - Legal Technology

- We need two banners (same style) designed with two different images and different text.

- The details of the printing requirements are attached, along with suggested images.

- The banners should share the same theme as our website www.brightcounsel.com.au

- The first banner would include our logo (attached), use the 'roads join' image (attached) in some way and text: New Opportunities - Where legal services and technology meet.

- The second banner would include our logo (attached), use the 'jigsaw' image (attached) in some way and use text: Legal Technology Strategy, Advice and Capability.

- Details on what are required from the Printer is attached also.

Target Market(s)

Legal Professionals

Industry/Entity Type

Information Technology

Font styles to use
Sans Serif

Requirements
Must have
• Our logo (attached), suggested text and the image mentioned for each.
Nice to have
• Professional and modern look
Should not have
• Cheap looking

```html
<!DOCTYPE html>
<html lang="en">
<head>
<meta charset="utf-8">
<title>BrightCounsel – Popup Banners</title>
<link rel="stylesheet" href="https://fonts.googleapis.com/css2?family=Fira+Sans+Condensed:ital,wght@0,300;1,300;1,600&display=swap">
<style>
  :root {
    --page: #ffffff;
    --ink: #ffffff;
    --sky-top: #2f78b8;
    --sky-mid: #3f8fc2;
    --horizon: #2a6a86;
    --field: #3f7d33;
    --field-dark: #2d5a26;
    --path: #8f7a4a;
    --puzzle-deep: #153a58;
    --puzzle-mid: #2c5f85;
    --puzzle-light: #a9c4d8;
  }
  * { margin: 0; padding: 0; box-sizing: border-box; }
  html, body {
    width: 1200px; height: 1000px; overflow: hidden;
    background: var(--page);
  }
  .canvas { position: relative; width: 1200px; height: 1000px; }
  .banner {
    position: absolute; top: 0; width: 412px; height: 1000px;
    overflow: hidden; color: var(--ink);
    font-family: "Fira Sans Condensed", sans-serif;
  }
  .banner--roads { left: 122px; }
  .banner--jigsaw { left: 645px; }
  .banner__photo { position: absolute; inset: 0; }
  .banner--roads .banner__photo {
    background:
      linear-gradient(180deg, rgba(10,30,50,0.25) 0%, rgba(0,0,0,0) 30%),
      linear-gradient(180deg, var(--sky-top) 0%, var(--sky-mid) 35%, var(--horizon) 48%, var(--field-dark) 52%, var(--field) 68%, var(--path) 88%, var(--field-dark) 100%);
  }
  .banner--jigsaw .banner__photo {
    background:
      radial-gradient(ellipse at 60% 50%, var(--puzzle-light) 0%, var(--puzzle-mid) 45%, var(--puzzle-deep) 100%);
  }
  .headline {
    position: absolute; left: 0; width: 100%;
    text-align: center; font-style: italic; font-weight: 300;
    text-transform: uppercase; line-height: 1;
  }
  .headline span { display: block; }
  .banner--roads .headline { top: 78px; }
  .headline__lead { font-size: 50px; letter-spacing: 8px; }
  .headline__sub { font-size: 36px; letter-spacing: 6px; margin-top: 20px; }
  .headline__line { font-size: 38px; letter-spacing: 8px; margin-top: 14px; }
  .headline__line--first { margin-top: 44px; }
  .headline__accent { font-size: 48px; font-weight: 600; letter-spacing: 9px; margin-top: 12px; }
  .banner--jigsaw .headline { top: 346px; }
  .banner--jigsaw .headline__line { font-size: 46px; letter-spacing: 10px; margin-top: 18px; }
  .banner--jigsaw .headline__line:first-child { margin-top: 0; }
  .brand {
    position: absolute; left: 30px; bottom: 60px;
    display: flex; align-items: center; gap: 18px;
  }
  .brand__mark { width: 30px; height: 30px; background: var(--ink); }
  .brand__name {
    font-family: "Fira Sans Condensed", sans-serif;
    font-weight: 300; font-size: 32px; letter-spacing: 4px; color: var(--ink);
  }
</style>
</head>
<body>
<main class="canvas">
  <section class="banner banner--roads">
    <div class="banner__photo" role="img" aria-label="Photo of a dirt country road winding through a green meadow under a blue sky"></div>
    <h1 class="headline">
      <span class="headline__lead">New</span>
      <span class="headline__sub">Opportunities</span>
      <span class="headline__line headline__line--first">Where legal</span>
      <span class="headline__line">services and</span>
      <span class="headline__line">technology</span>
      <span class="headline__accent">meet.</span>
    </h1>
    <div class="brand">
      <span class="brand__mark"></span>
      <span class="brand__name">BrightCounsel</span>
    </div>
  </section>

  <section class="banner banner--jigsaw">
    <div class="banner__photo" role="img" aria-label="Photo of a hand placing a glowing jigsaw puzzle piece in blue light"></div>
    <h1 class="headline">
      <span class="headline__line">Legal</span>
      <span class="headline__line">Technology</span>
      <span class="headline__line">Strategy,</span>
      <span class="headline__line">Advice and</span>
      <span class="headline__line">Capability.</span>
    </h1>
    <div class="brand">
      <span class="brand__mark"></span>
      <span class="brand__name">BrightCounsel</span>
    </div>
  </section>
</main>
</body>
</html>
```